Pediatric Vision Care: Myopia Control Brochure

We are a pediatric eye care practice (ophthalmology and optometry). One of our services we offer for children is myopia control, which are strategies for slowing or stopping the progression of nearsightedness. This is a service we need to sell to parents because most insurance won't pay for it. There are different options we offer that can work well for kids in different situations: glasses with Corvane lenses, atropine eye drops, and/or special contact lenses. We need a brochure we can distribute to parents to let them know about this service that would encourage them to buy it for children who need it. Attached is our initial draft brochure created by our staff that provides text that we want to keep. The images and layout can change. We probably need at least one or two photos of kids on the brochure, because this is only something that works for children who are still growing, and the target audience is parents of 4-8 year old children.

Target Market(s)

Parents of 4-8 year old children

Font styles to use
Sans Serif

Requirements
Must have
• I'm uploading our company logo that should be included somewhere on the brochure. You can include contact information (web address, phone number) for our practice that is found on our website: http://www.brookhollowkidsvision.com/
Should not have
• This should not look childish. We need the impression to be friendly but professional, medical, expert.

```html
<!DOCTYPE html>
<html lang="en">
<head>
<meta charset="utf-8">
<title>Myopia Control Brochure – Brookhollow Kids Vision</title>
<link href="https://fonts.googleapis.com/css2?family=Montserrat:ital,wght@0,400;0,500;0,600;0,700;0,800;1,400&display=swap" rel="stylesheet">
<style>
:root{
  --stage:#3d4350;
  --navy:#0d47a1;
  --blue:#1257b5;
  --deep:#0a3596;
  --sky:#dbeafc;
  --pale:#eef5fd;
  --green:#3f9a1e;
  --green-dark:#2f7d17;
  --orange:#f5860f;
  --yellow:#ffe100;
  --ink:#222831;
  --white:#ffffff;
  --violet:#5f6ed6;
}
*{box-sizing:border-box;margin:0;padding:0}
html,body{width:863px;height:1200px;overflow:hidden}
body{background:var(--stage);font-family:'Montserrat',sans-serif;color:var(--ink);position:relative}
.sheet{position:absolute;left:77px;width:709px;height:546px;overflow:hidden;background:var(--white)}
.sheet--outside{top:47px}
.sheet--inside{top:607px}
.panel{position:absolute;top:0;height:100%;width:236.3px}
.p1{left:0}.p2{left:236.3px;border-left:1px solid #c9d6e6}.p3{left:472.6px;border-left:1px solid #c9d6e6}
.abs{position:absolute}
.photo{position:absolute}
.h-bar{position:absolute;height:14px;background:var(--navy)}
.h-bar.green{background:var(--green)}
.title-blue{color:var(--navy);font-weight:700}
.small{font-size:6.1px;line-height:9.4px;color:var(--ink)}

/* outside left */
.p1-out{background:linear-gradient(180deg,#c8def8 0%,#eaf3fd 45%,#f7fbff 100%)}
.why-title{left:31px;top:32px;font-size:14.5px}
.reason{position:absolute;left:17px;width:205px}
.reason .tick{position:absolute;left:0;top:0}
.reason h3{margin-left:24px;font-size:10.4px;line-height:11px;color:var(--navy);font-weight:600}
.reason p{margin-left:24px;margin-top:5px;width:165px;font-size:6px;line-height:9.4px}
.schedule{left:30px;top:428px;width:176px;height:62px;background:var(--navy);border-radius:7px;color:var(--white)}
.schedule strong{position:absolute;left:53px;top:10px;font-size:10px;line-height:15px;font-weight:700}
.schedule span{position:absolute;left:14px;top:47px;font-size:6px}

/* outside middle */
.p2-out{background:linear-gradient(180deg,#e9f2fd 0%,#ffffff 40%,#ffffff 100%)}
.brand{position:absolute;display:flex;align-items:center;gap:6px;font-weight:600;color:#1c2a3a;white-space:nowrap}
.brand i{display:block;width:13px;height:13px;border-radius:50%;background:var(--green);flex:none}
.contact-title{left:100px;top:210px;width:130px;text-align:center;font-size:14.5px;line-height:15px;color:var(--blue);font-weight:700}
.contact-rule{left:182px;top:261px;width:37px;height:1.5px;background:var(--blue)}
.c-line{position:absolute;left:0;width:236px;text-align:center;font-size:10px;font-weight:700;color:var(--navy)}
.c-icon{position:absolute;left:112px}

/* outside right */
.hero-title{left:20px;top:8px;font-size:37px;line-height:41px;font-weight:700;color:var(--navy)}
.hero-sub{left:20px;top:90px;font-size:25px;font-weight:500;color:var(--green)}
.hero-rule{left:21px;top:127px;width:64px;height:1.5px;background:var(--blue)}
.hero-tag{left:22px;top:134px;font-size:10px;line-height:15.5px;width:100px;color:#1e1e1e}
.badge{left:0;top:376px;width:145px;height:76px;background:var(--navy);border-radius:0 8px 8px 8px;color:var(--white)}
.badge p{position:absolute;left:58px;top:4px;font-size:10px;line-height:15.5px;font-weight:400}
.badge b{font-size:22px;color:var(--yellow);font-weight:800}

/* inside */
.sec-title{font-size:15px;font-weight:700;color:var(--navy)}
.env-item h4{font-size:10.3px;font-weight:600}
.card{position:absolute;border-radius:7px;background:linear-gradient(180deg,#bed8f7 0%,#e6f0fc 45%,#f4f8fd 100%)}
.card-title{position:absolute;left:0;width:100%;text-align:center;font-size:10.5px;line-height:11px;font-weight:700}
.icon-ring{position:absolute;width:34px;height:34px;border-radius:50%;background:var(--white);border:2px solid var(--navy)}
.tag{position:absolute;height:11px;padding:0 8px;font-size:7.6px;line-height:11px;font-weight:700;color:var(--white);border-radius:2px;text-align:center}
.strip{position:absolute;bottom:0;height:10px;width:236.3px}
.treat-title{left:28px;top:20px;width:180px;text-align:center;font-size:14px;line-height:15px;white-space:nowrap;letter-spacing:-0.2px}
</style>
</head>
<body>

<section class="sheet sheet--outside">
  <div class="panel p1 p1-out">
    <div class="h-bar" style="left:0;top:36px;width:28px"></div>
    <h2 class="abs title-blue why-title">Why start early?</h2>

    <div class="reason" style="top:74px">
      <svg class="tick" width="17" height="17" viewBox="0 0 20 20"><circle cx="10" cy="10" r="10" fill="#3f9a1e"/><path d="M5 10.5l3.3 3.3L15 7" stroke="#fff" stroke-width="2.6" fill="none"/></svg>
      <h3>Myopia worsens as children grow.</h3>
      <p>The eye continues to elongate during childhood, increasing the glasses prescription.</p>
    </div>
    <div class="reason" style="top:128px">
      <svg class="tick" width="17" height="17" viewBox="0 0 20 20"><circle cx="10" cy="10" r="10" fill="#3f9a1e"/><path d="M5 10.5l3.3 3.3L15 7" stroke="#fff" stroke-width="2.6" fill="none"/></svg>
      <h3>Higher risk of serious eye problems.</h3>
      <p>More severe myopia is associated with a higher risk of retinal problems and macular degeneration in adulthood.</p>
    </div>
    <div class="reason" style="top:202px">
      <svg class="tick" width="17" height="17" viewBox="0 0 20 20"><circle cx="10" cy="10" r="10" fill="#3f9a1e"/><path d="M5 10.5l3.3 3.3L15 7" stroke="#fff" stroke-width="2.6" fill="none"/></svg>
      <h3>Early treatment = better long - term vision.</h3>
      <p>Slowing progression now helps protect your child's vision for the future.</p>
    </div>

    <div class="photo" role="img" aria-label="Eye doctor examining a smiling young boy at a slit lamp, with an eye chart behind"
         style="left:0;top:260px;width:236px;height:240px;background:linear-gradient(135deg,#e4e8ee 0%,#c9b9a8 40%,#8a6a55 65%,#4c6f98 100%)"></div>
    <svg class="abs" style="left:0;top:440px" width="237" height="106" viewBox="0 0 237 106" preserveAspectRatio="none">
      <path d="M0 40 C60 85 150 80 237 45 L237 106 L0 106Z" fill="#f2f7fe"/>
      <path d="M0 96 C80 100 170 85 237 55 L237 106 L0 106Z" fill="#0d3fa0"/>
    </svg>

    <div class="abs schedule">
      <svg class="abs" style="left:13px;top:8px" width="32" height="32" viewBox="0 0 32 32"><rect x="2" y="4" width="28" height="26" rx="3" fill="none" stroke="#fff" stroke-width="2"/><path d="M2 11h28M9 1v6M23 1v6" stroke="#fff" stroke-width="2"/><g fill="#fff"><rect x="7" y="15" width="4" height="3"/><rect x="14" y="15" width="4" height="3"/><rect x="21" y="15" width="4" height="3"/><rect x="7" y="21" width="4" height="3"/><rect x="14" y="21" width="4" height="3"/><rect x="21" y="21" width="4" height="3"/></g></svg>
      <strong>Schedule your child's<br>evaluation today!</strong>
      <span>The sooner we start, the more we can protect.</span>
    </div>
  </div>

  <div class="panel p2 p2-out">
    <div class="brand" style="left:22px;top:56px;font-size:14px"><i></i>Brookhollow Kids Vision</div>
    <div class="photo" role="img" aria-label="Portrait of the practice's smiling optician in a white coat, eyewear display behind"
         style="left:0;top:98px;width:100px;height:200px;background:linear-gradient(180deg,#e8eef6 0%,#d9c2a8 40%,#f2f2f2 75%,rgba(255,255,255,0) 100%)"></div>
    <h2 class="abs contact-title">Contact and scheduling info</h2>
    <div class="abs contact-rule"></div>

    <svg class="c-icon" style="top:271px" width="12" height="13" viewBox="0 0 24 24"><path d="M6.6 10.8a15 15 0 006.6 6.6l2.2-2.2c.3-.3.7-.4 1-.2 1.1.4 2.3.6 3.6.6.6 0 1 .4 1 1V20c0 .6-.4 1-1 1C10.6 21 3 13.4 3 4c0-.6.4-1 1-1h3.5c.6 0 1 .4 1 1 0 1.3.2 2.5.6 3.6.1.3 0 .7-.2 1z" fill="#f5860f"/></svg>
    <div class="c-line" style="top:298px">(555) 014-2280</div>
    <svg class="c-icon" style="top:323px" width="12" height="13" viewBox="0 0 24 24"><path d="M12 2a7 7 0 00-7 7c0 5.2 7 13 7 13s7-7.8 7-13a7 7 0 00-7-7zm0 9.5A2.5 2.5 0 1112 6.5a2.5 2.5 0 010 5z" fill="#f5860f"/></svg>
    <div class="c-line" style="top:345px;line-height:15.6px">Brookhollow Kids Vision<br>218 Maple Crest Drive<br>Fairhaven, VA 23400</div>
    <svg class="c-icon" style="top:404px" width="11" height="9" viewBox="0 0 24 18"><rect width="24" height="18" rx="2" fill="#f5860f"/><path d="M1 2l11 8 11-8" stroke="#fff" stroke-width="2" fill="none"/></svg>
    <div class="c-line" style="top:424px;font-size:9.2px">appointments@brookhollowkidsvision.com</div>

    <svg class="abs" style="left:0;top:450px" width="237" height="96" viewBox="0 0 237 96" preserveAspectRatio="none">
      <defs><linearGradient id="waveBlue" x1="0" y1="0" x2="0" y2="1"><stop offset="0" stop-color="#0f4fb0"/><stop offset="1" stop-color="#0733a0"/></linearGradient></defs>
      <path d="M0 50 C70 20 140 -10 237 20 L237 96 L0 96Z" fill="url(#waveBlue)"/>
    </svg>
    <svg class="c-icon" style="top:487px" width="11" height="11" viewBox="0 0 24 24"><circle cx="12" cy="12" r="10" fill="none" stroke="#f5860f" stroke-width="2.4"/><path d="M2 12h20M12 2c3 3 3 17 0 20M12 2c-3 3-3 17 0 20" stroke="#f5860f" stroke-width="2" fill="none"/></svg>
    <div class="c-line" style="top:507px;color:#fff">brookhollowkidsvision.com</div>
  </div>

  <div class="panel p3">
    <div class="photo" role="img" aria-label="Smiling girl with red hair wearing dark-framed glasses, outdoors in a sunny park"
         style="left:0;top:0;width:237px;height:546px;background:radial-gradient(ellipse at 72% 62%,#e4b396 0%,#c88556 28%,#b6773d 42%,rgba(160,190,120,.9) 60%,#cfe2f5 85%),linear-gradient(180deg,#cfe2f8,#9fbf7f)"></div>
    <svg class="abs" style="left:0;top:0" width="237" height="546" viewBox="0 0 237 546" preserveAspectRatio="none">
      <defs><linearGradient id="fadeTop" x1="0" y1="0" x2="1" y2="0"><stop offset="0" stop-color="#ddebfb"/><stop offset=".55" stop-color="#ddebfb" stop-opacity=".85"/><stop offset="1" stop-color="#ddebfb" stop-opacity="0"/></linearGradient></defs>
      <rect width="237" height="190" fill="url(#fadeTop)"/>
      <path d="M0 470 C40 440 90 425 130 440 C180 455 215 480 237 486 L237 546 L0 546Z" fill="#fff"/>
      <path d="M90 455 C140 448 200 470 237 486 L237 546 L60 546Z" fill="#fff"/>
    </svg>
    <h1 class="abs hero-title">Myopia<br>Control</h1>
    <div class="abs hero-sub">for childern</div>
    <div class="abs hero-rule"></div>
    <p class="abs hero-tag">Protect your child's vision for the future</p>

    <div class="abs badge">
      <svg class="abs" style="left:8px;top:14px" width="42" height="48" viewBox="0 0 42 48"><path d="M21 2L39 8v14c0 12-8 20-18 24C11 42 3 34 3 22V8z" fill="#fff"/><path d="M21 7L34 11.5v10.5c0 9-6 15-13 18-7-3-13-9-13-18V11.5z" fill="#3f9a1e"/><path d="M13 24l6 6 10-12" stroke="#fff" stroke-width="4" fill="none" stroke-linecap="round"/></svg>
      <p>Slow<br>down myopia<br>progression by<br>up to <b>50%</b></p>
    </div>
    <div class="brand" style="left:20px;top:504px;font-size:14.5px"><i></i>Brookhollow Kids Vision</div>
  </div>
</section>

<section class="sheet sheet--inside">
  <div class="panel p1">
    <div class="h-bar" style="left:0;top:23px;width:28px"></div>
    <h2 class="abs sec-title" style="left:31px;top:20px">Myopia Control</h2>
    <p class="abs small" style="left:31px;top:57px;width:180px">Myopia or nearsightedness causes blurry distance vision. Myopia is caused by the elongation of the eye, and progresses throughout childhood. Myopia is becoming increasingly common. More severe myopia and a higher glasses prescription is associated with a higher risk of eye problems involving the retina in adulthood, such as retinal problems and macular degeneration.<br>Myopia control is meant to slow the growth of the eye, keeping the glasses prescription as low as possible and reducing the risk of ocular disease in adulthood.<br>There are several treatment options .</p>

    <div class="h-bar green" style="left:0;top:184px;width:28px"></div>
    <h2 class="abs sec-title" style="left:31px;top:181px;color:var(--green)">Environmental options:</h2>
    <p class="abs" style="left:32px;top:199px;font-size:6.2px;font-style:italic">All myopic children can benefit from these lifestyle changes.</p>

    <div class="abs env-item" style="left:14px;top:229px">
      <svg class="abs" style="left:0;top:0" width="17" height="17" viewBox="0 0 20 20"><circle cx="10" cy="10" r="10" fill="#3f9a1e"/><circle cx="10" cy="10" r="5" fill="#ffe100"/></svg>
      <h4 style="margin-left:23px;margin-top:1px;color:var(--green);white-space:nowrap">Get outdoors!</h4>
    </div>
    <p class="abs small" style="left:38px;top:257px;width:128px">It is important to get your child outdoors consistently. There is strong evidence that children who spend at least 2 hours a day outdoors are less likely to become myopic, and their myopia progresses slower than children who are outdoors less. Some studies show that increasing outdoor time by as few as 45 minutes a day is beneficial in reducing progression.</p>
    <div class="photo" role="img" aria-label="Boy running across a sunny park lawn" style="left:168px;top:230px;width:64px;height:106px;border-radius:3px;background:linear-gradient(180deg,#3f6a2a 0%,#5e8f3a 45%,#86b552 100%)"></div>

    <div class="abs env-item" style="left:13px;top:356px">
      <svg class="abs" style="left:0;top:0" width="17" height="17" viewBox="0 0 20 20"><circle cx="10" cy="10" r="10" fill="#0d47a1"/><rect x="5" y="6" width="10" height="7" fill="none" stroke="#fff" stroke-width="1.4"/><path d="M7 15h6" stroke="#fff" stroke-width="1.4"/></svg>
      <h4 style="margin-left:23px;margin-top:1px;color:var(--navy);white-space:nowrap">Limit screen time</h4>
    </div>
    <p class="abs small" style="left:36px;top:383px;width:125px">There is some evidence that consistent use of screens, particularly held very close to the face, can worsen nearsightedness.</p>
    <div class="photo" role="img" aria-label="Child under a blanket lit by a tablet screen" style="left:168px;top:356px;width:64px;height:59px;border-radius:3px;background:radial-gradient(ellipse at 50% 55%,#8fa6c3 0%,#3f5371 45%,#1a2536 100%)"></div>

    <div class="abs env-item" style="left:15px;top:434px">
      <svg class="abs" style="left:0;top:0" width="17" height="17" viewBox="0 0 20 20"><circle cx="10" cy="10" r="9" fill="#fff" stroke="#5f6ed6" stroke-width="2"/><path d="M10 4v6l4 2" stroke="#5f6ed6" stroke-width="1.6" fill="none"/></svg>
      <h4 style="margin-left:23px;margin-top:1px;color:var(--violet);white-space:nowrap">Use the 20-20-20 rule</h4>
    </div>
    <p class="abs small" style="left:38px;top:461px;width:125px">We recommend limiting nonacademic screen time and near work, and encourage your child to use the 20-20-20 rule. Every 20 minutes take a 20 second break to look at least 20 feet away.</p>
    <div class="photo" role="img" aria-label="Digital alarm clock on a bedside table beside a plant" style="left:168px;top:435px;width:64px;height:78px;border-radius:3px;background:linear-gradient(180deg,#3d4a2d 0%,#6a5638 55%,#2a2218 100%)"></div>

    <div class="strip" style="left:0;background:var(--green)"></div>
  </div>

  <div class="panel p2">
    <div class="h-bar" style="left:0;top:23px;width:27px"></div>
    <div class="h-bar" style="left:209px;top:23px;width:27px"></div>
    <h2 class="abs sec-title treat-title">Proven Myopia Control<br>Treatments</h2>
    <p class="abs" style="left:30px;top:57px;width:176px;text-align:center;font-size:12px;line-height:13px;color:var(--green)">Customized for<br>your child.</p>

    <div class="card" style="left:20px;top:134px;width:196px;height:288px">
      <div class="card-title" style="top:22px;color:var(--navy)">Lumera<sup style="font-size:6px">®</sup> Corvane<sup style="font-size:6px">®</sup><br>glasses lenses</div>
      <div class="photo" role="img" aria-label="Glasses lens with concentric micro-lenslet rings on a teal background" style="left:8px;top:53px;width:183px;height:124px;background:radial-gradient(ellipse at 55% 55%,#5fa7aa 0%,#2f7d83 50%,#1c5358 100%)"></div>
      <span class="abs" style="left:16px;top:56px;font-size:13px;color:#fff;font-weight:400">Corvane</span>
      <p class="abs small" style="left:8px;top:183px;width:182px">FDA market authorized Lumera Corvane glasses lenses have been shown to slow myopia progression by about 50% in children aged 6-12.</p>
      <p class="abs small" style="left:8px;top:215px;width:182px">These lenses are a great treatment option because all your child needs to do is wear glasses. They look almost identical to ordinary glasses, but use specialized optics to signal the brain to slow the growth of myopic eyes.</p>
      <div class="tag" style="left:58px;top:268px;width:80px;background:var(--navy)">FDA approved</div>
    </div>
    <div class="icon-ring" style="left:101px;top:116px">
      <svg class="abs" style="left:4px;top:9px" width="22" height="12" viewBox="0 0 22 12"><circle cx="5" cy="6" r="4" fill="none" stroke="#0d47a1" stroke-width="1.4"/><circle cx="17" cy="6" r="4" fill="none" stroke="#0d47a1" stroke-width="1.4"/><path d="M9 6h4" stroke="#0d47a1" stroke-width="1.4"/></svg>
    </div>

    <div class="abs" style="left:27px;top:482px;width:182px;height:35px;background:linear-gradient(90deg,#dfeafa,#f4f8fe)"></div>
    <div class="photo" role="img" aria-label="Doctor illustration in a white coat with stethoscope" style="left:29px;top:482px;width:36px;height:35px;background:linear-gradient(180deg,#c9d8ec 0%,#e8eef7 100%)"></div>
    <p class="abs" style="left:67px;top:483px;width:140px;font-size:8.5px;line-height:10.4px;color:var(--blue)">Your doctor will recommend the best option based on your child's needs and your family's lifestyle.</p>

    <div class="strip" style="left:0;background:var(--navy)"></div>
  </div>

  <div class="panel p3">
    <div class="card" style="left:20px;top:34px;width:197px;height:227px">
      <div class="card-title" style="top:22px;color:var(--green)">Low - dose antropine</div>
      <div class="photo" role="img" aria-label="Eye dropper releasing a single drop against a dark teal background" style="left:7px;top:42px;width:183px;height:76px;background:linear-gradient(90deg,#dfe7ea 0%,#3f6775 35%,#2a4b58 100%)"></div>
      <p class="abs small" style="left:7px;top:125px;width:182px">These eyedrops have been studied for over 20 years and have been shown to slow myopia progression by about 50% when used consistently.</p>
      <p class="abs small" style="left:7px;top:157px;width:182px">Low-dose atropine is simple to add to your daily routine. One drop is placed in each eye before bed each evening. These are ordered from a compounding pharmacy and mailed directly to your home.</p>
      <div class="tag" style="left:48px;top:205px;width:101px;background:var(--green-dark)">20+ years of research</div>
    </div>
    <div class="icon-ring" style="left:101px;top:15px;border-color:var(--green)">
      <svg class="abs" style="left:8px;top:5px" width="14" height="20" viewBox="0 0 14 20"><path d="M7 1C5 6 1 9 1 13a6 6 0 0012 0c0-4-4-7-6-12z" fill="#3f9a1e"/></svg>
    </div>

    <div class="card" style="left:20px;top:292px;width:197px;height:229px">
      <div class="card-title" style="top:22px;color:var(--orange)">Low - dose antropine</div>
      <div class="photo" role="img" aria-label="Soft contact lens balanced on a fingertip against black" style="left:7px;top:41px;width:183px;height:88px;background:linear-gradient(90deg,#7a4a35 0%,#b87d62 30%,#3b6f9a 40%,#000 50%,#000 100%)"></div>
      <p class="abs small" style="left:7px;top:135px;width:182px">FDA-approved ClearStep lenses have been shown to slow myopia progression by about 50% in children aged 8-12.</p>
      <p class="abs small" style="left:7px;top:157px;width:182px">Contact lenses can be a great fit for many children, especially active children or those who do not enjoy wearing glasses. Many children as young as 7 or 8 are successful at wearing contacts.</p>
      <div class="tag" style="left:48px;top:209px;width:101px;background:var(--orange)">Great for active kids</div>
    </div>
    <div class="icon-ring" style="left:101px;top:273px;border-color:var(--orange)">
      <svg class="abs" style="left:5px;top:8px" width="20" height="14" viewBox="0 0 20 14"><path d="M1 7c3-6 15-6 18 0" fill="none" stroke="#f5860f" stroke-width="1.6"/><path d="M2 8c3 5 13 5 16 0" fill="none" stroke="#f5860f" stroke-width="1.6"/></svg>
    </div>

    <div class="strip" style="left:0;background:var(--orange)"></div>
  </div>
</section>

</body>
</html>
```